The Corvane Agency

We are a pr, social media and strategy agency specializing in the pet industry. We would like a new dynamic design of our existing website. We think it is currently outdated and looks too corporate. We would like it to look more consumer oriented as we primarily market pet products. We would like warm imagery involving pets and while pets are fun, this is still a business website and needs to maintain a professional look. We are hired by business owners and executives.
I would like some of our work featured on the home page.
Our primary service tabs are:
Public Relations
Social Media
Product Consulting
Most of the content will remain the same but we are open to suggestions!
Our current website can be found at www.corvanepetpr.example.
We are open to other colors than in our logo and on our current page.
This is a design only project and will not require programming. The selected designer will need to provide at least one interior page in addition to the home page.

Industry/Entity Type

Pet

Requirements
Should not have
• Cartoon type figures. Pet puns.

```html
<!DOCTYPE html>
<html lang="en">
<head>
<meta charset="utf-8">
<title>The Corvane Agency</title>
<link href="https://fonts.googleapis.com/css2?family=Open+Sans:wght@400;600;700&display=swap" rel="stylesheet">
<style>
:root{
  --red:#e3201b;
  --ink:#2a2a2a;
  --grey-text:#8a8a8a;
  --band:#e4e4e4;
  --nav:#f5f5f5;
  --panel:#6e6e6e;
  --footer:#141414;
  --white:#ffffff;
}
*{margin:0;padding:0;box-sizing:border-box}
html,body{width:821px;height:1200px;overflow:hidden}
body{font-family:'Open Sans',Arial,sans-serif;color:var(--ink);background:var(--white);position:relative}
.abs{position:absolute}

/* header */
.top-band{left:0;top:0;width:821px;height:60px;background:var(--band)}
.nav-band{left:0;top:60px;width:821px;height:38px;background:var(--nav);border-bottom:1px solid #ddd}
.logo-box{left:89px;top:0;width:161px;height:98px;background:var(--white);display:flex;align-items:center;justify-content:center}
.logo-name{color:var(--red);font-size:15px;font-weight:600;text-align:center;line-height:1.1}
.nav{left:250px;top:60px;height:38px;display:flex}
.nav a{display:flex;align-items:center;padding:0 11px;font-size:10px;color:#666;text-decoration:none;border-right:1px solid #ddd;text-transform:uppercase}
.nav a.active{background:var(--red);color:var(--white);padding:0 11px}
.enquiry{left:582px;top:16px;display:flex;align-items:center;gap:7px}
.enquiry-label{font-size:8.5px;color:#666;line-height:1}
.enquiry-number{font-size:13px;color:var(--red);line-height:1.2}
.globe{left:710px;top:17px}

/* hero */
.hero{left:0;top:98px;width:821px;height:313px;background:radial-gradient(ellipse at 20% 45%,#8a8a8a 0%,#3a3a3a 35%,#1a1a1a 70%),#111}
.hero-copy{left:323px;top:192px;color:var(--white);text-transform:uppercase}
.hero-l1{font-size:27px;font-weight:600;line-height:1}
.hero-l2{font-size:42px;font-weight:600;color:var(--red);line-height:.95}
.hero-l3{font-size:27px;font-weight:600;line-height:1}
.hero-tag{font-size:11.5px;font-weight:600;margin-top:4px;margin-left:2px}
.hero-more{left:566px;top:314px;font-size:8.5px;font-weight:700;color:var(--red)}
.dots{left:648px;top:374px;display:flex;gap:14px}
.dots span{width:9px;height:9px;border-radius:50%;background:var(--white)}
.dots span.on{background:var(--red);box-shadow:0 0 0 2px #fff}

/* about */
.about{left:0;top:411px;width:821px;height:306px;background:var(--band)}
.about-title{left:0;top:444px;width:821px;text-align:center;color:var(--red);font-size:15.5px}
.about-text{left:120px;top:479px;width:581px;text-align:center;font-size:11.6px;line-height:14px;color:#555}

/* services */
.card{top:634px;width:210px;height:216px;background:var(--white);border:1px solid #e6e6e6}
.card-photo{position:absolute;left:49px;top:-42px;width:112px;height:112px;border-radius:50%;border:3px solid #fff}
.card-title{position:absolute;left:0;top:92px;width:100%;text-align:center;font-size:13px;letter-spacing:.3px}
.card-text{position:absolute;left:21px;top:124px;width:170px;font-size:8.3px;line-height:11px;color:var(--grey-text)}
.card-more{position:absolute;right:0;bottom:8px;width:52px;height:17px;background:var(--red);color:var(--white);font-size:9.5px;font-style:italic;display:flex;align-items:center;justify-content:center}

/* testimonial & contact */
.panel{top:882px;height:131px;background:var(--panel);color:var(--white)}
.pointer{left:369px;top:1013px}
.round-photo{position:absolute;width:100px;height:100px;border-radius:50%;border:2px solid #fff}
.quote{position:absolute;left:133px;top:24px;width:168px;font-size:8.5px;line-height:11px}
.quote-name{position:absolute;left:128px;top:88px;font-size:11px;font-weight:600;line-height:12px}
.quote-org{font-size:8.5px;font-weight:400}
.contact-title{position:absolute;left:154px;top:18px;font-size:15px}
.contact-lines{position:absolute;left:154px;top:51px;font-size:8.5px;line-height:11px}

/* footer */
.footer{left:0;top:1066px;width:821px;height:134px;background:var(--footer)}
.link-col{top:1092px}
.link-col h4{font-weight:400;font-size:12px;color:var(--red);margin-bottom:4px}
.link-col li{list-style:none;font-size:10.5px;line-height:12.2px;color:#8a8a8a}
.footer-rule{left:289px;top:1085px;width:1px;height:100px;background:#333}
.social{left:587px;top:1099px;display:flex;align-items:center;gap:6px}
.social-label{color:var(--red);font-size:12px;margin-right:6px}
.social-dot{width:22px;height:22px;border-radius:50%;background:#8c8c8c}
.footer-line{left:319px;top:1160px;width:414px;height:1px;background:#333}
.copyright{left:319px;top:1170px;width:414px;text-align:right;font-size:9px;color:#777}
</style>
</head>
<body>

<header>
  <div class="abs top-band"></div>
  <div class="abs nav-band"></div>
  <div class="abs logo-box"><div class="logo-name">The Corvane<br>Agency</div></div>
  <nav class="abs nav">
    <a class="active" href="#">PR</a>
    <a href="#">Social Media</a>
    <a href="#">Pet Express</a>
    <a href="#" style="padding:0 11px">Business Development</a>
    <a href="#">Case Studies</a>
    <a href="#">Our Team</a>
  </nav>
  <div class="abs enquiry">
    <svg width="13" height="20" viewBox="0 0 13 20"><rect x="1" y="1" width="11" height="18" rx="2" fill="none" stroke="#222" stroke-width="2"/><rect x="3" y="4" width="7" height="10" fill="#222"/></svg>
    <div>
      <div class="enquiry-label">call us for enquiries</div>
      <div class="enquiry-number">000555012345</div>
    </div>
  </div>
  <svg class="abs globe" width="22" height="22" viewBox="0 0 22 22"><circle cx="11" cy="11" r="10" fill="none" stroke="#222" stroke-width="2"/><ellipse cx="11" cy="11" rx="4" ry="10" fill="none" stroke="#222" stroke-width="1.5"/><line x1="1" y1="11" x2="21" y2="11" stroke="#222" stroke-width="1.5"/></svg>
</header>

<section>
  <div class="abs hero" role="img" aria-label="Black and white photo of a kitten sitting in front of a desktop computer"></div>
  <div class="abs hero-copy">
    <div class="hero-l1">Redefining</div>
    <div class="hero-l2">The Pet</div>
    <div class="hero-l3">Industry</div>
    <div class="hero-tag">There is noting more than a loyal good pet...</div>
  </div>
  <div class="abs hero-more">RED MORE</div>
  <div class="abs dots"><span class="on"></span><span></span><span></span><span></span></div>
</section>

<section>
  <div class="abs about"></div>
  <h2 class="abs about-title" style="font-weight:400">ABOUT CORVANE</h2>
  <p class="abs about-text">PR has evolved from public relations to personal relations. As new communication tools have emerged, old habits have been buried, giving way to the consumer revolution of social media. At Corvane, we tap the best ways to connect you with those in the pet industry. That focus makes our team your ideal partner for creating a community as faithful as a favorite pet.</p>
</section>

<section>
  <div class="abs card" style="left:91px">
    <div class="card-photo" role="img" aria-label="Photo of a smiling businesswoman in front of a crowd" style="background:radial-gradient(circle at 50% 45%,#d9a08a,#5a3a32 70%)"></div>
    <div class="card-title">PUBLIC RELATIONS</div>
    <div class="card-text">The driving force behind our success is the team that makes it happen. Individual skills and experience meet a collective desire to excel...</div>
    <div class="card-more">more...</div>
  </div>
  <div class="abs card" style="left:306px">
    <div class="card-photo" role="img" aria-label="Photo of a finger pressing a keyboard of social network keys" style="background:radial-gradient(circle at 50% 40%,#f2f2f2,#9fb3c8 75%)"></div>
    <div class="card-title">SOCIAL MEDIA</div>
    <div class="card-text">The driving force behind our success is the team that makes it happen. Individual skills and experience meet a collective desire to excel...</div>
    <div class="card-more">more...</div>
  </div>
  <div class="abs card" style="left:522px">
    <div class="card-photo" role="img" aria-label="Black and white photo of two businessmen meeting at a table" style="background:radial-gradient(circle at 50% 40%,#e0e0e0,#333 80%)"></div>
    <div class="card-title" style="top:94px">PRODUCT CONSULTING</div>
    <div class="card-text">The driving force behind our success is the team that makes it happen. Individual skills and experience meet a collective desire to excel...</div>
    <div class="card-more">more...</div>
  </div>
</section>

<section>
  <div class="abs panel" style="left:89px;width:318px">
    <div class="round-photo" role="img" aria-label="Portrait photo of a smiling man in a suit" style="left:13px;top:13px;background:radial-gradient(circle at 50% 40%,#fff,#c9c9c9 60%,#2a3140 90%)"></div>
    <p class="quote">The only time I've had the privilege of working with designers like this was a specific time during my tenure at Norvik - while working on a new software project directly with Alan Pryce.</p>
    <div class="quote-name">- Martin Hale, President<br><span class="quote-org">National Pet Trade Council (NPTC)</span></div>
  </div>
  <svg class="abs pointer" width="22" height="24" viewBox="0 0 22 24"><polygon points="0,0 20,0 0,22" fill="#6e6e6e"/></svg>
  <div class="abs panel" style="left:416px;width:317px">
    <div class="round-photo" role="img" aria-label="Photo of customer service staff on phones" style="left:22px;top:13px;background:radial-gradient(circle at 60% 45%,#e8c9b5,#5a4038 75%)"></div>
    <div class="contact-title">Quick contact</div>
    <div class="contact-lines">Phone : 555010247788<br>email:&nbsp; hello@corvane.example<br>skype : corvane.desk<br><br>www.corvanepetpr.example</div>
  </div>
</section>

<footer>
  <div class="abs footer"></div>
  <div class="abs link-col" style="left:89px">
    <h4>Quick links</h4>
    <ul><li>contact</li><li>careers</li><li>blog</li><li>lovelist</li><li>sitemap</li></ul>
  </div>
  <div class="abs link-col" style="left:179px">
    <h4>Usefull links</h4>
    <ul><li>Like us</li><li>Follow us</li><li>Corvane life</li><li>Connect with us</li><li>Corporate site</li></ul>
  </div>
  <div class="abs footer-rule"></div>
  <div class="abs social">
    <span class="social-label">Social</span>
    <span class="social-dot"></span><span class="social-dot"></span><span class="social-dot"></span><span class="social-dot"></span>
  </div>
  <div class="abs footer-line"></div>
  <div class="abs copyright">© Copyright 2014 . All rights reserved to corvanepetpr</div>
</footer>

</body>
</html>
```